Looking to design a new sign for our church.

Looking for a new sign
4 x 8 feet dimension
We are renaming the church "Keller Ridge Community Church"
looking for legible graphics
Would like some type of backdrop being a family tree (oak) / open to other ideas as you are led
I have included a pic of the old sign for your review
would like to incorporate our ministry logo on the lower right hand corner of the sign / see file attached

```html
<!DOCTYPE html>
<html lang="en">
<head>
<meta charset="UTF-8">
<title>Keller Ridge Community Church Sign</title>
<link href="https://fonts.googleapis.com/css2?family=Montserrat:wght@600;800&display=swap" rel="stylesheet">
<style>
  :root {
    --page-bg: #eceae4;
    --sky-light: #fbf3d6;
    --sky-warm: #eedb9c;
    --bark: #c9a247;
    --grass: #2f5a1f;
    --grass-light: #4f8a2c;
    --band: #1f3a1b;
    --title-ink: #2b2410;
    --info-text: #f4f1e6;
  }
  * { margin: 0; padding: 0; box-sizing: border-box; }
  html, body { width: 1200px; height: 1122px; overflow: hidden; }
  body {
    background: var(--page-bg);
    display: flex;
    align-items: center;
    justify-content: center;
  }
  .church-sign {
    position: relative;
    width: 1100px;
    height: 598px;
    overflow: hidden;
    box-shadow: 0 6px 24px rgba(0,0,0,0.18);
  }
  .backdrop-art {
    position: absolute;
    inset: 0 0 178px 0;
    background: radial-gradient(ellipse at 50% 65%, var(--sky-light) 0%, var(--sky-warm) 55%, var(--bark) 100%);
  }
  .grass-edge {
    position: absolute;
    left: 0; right: 0;
    bottom: 178px;
    height: 46px;
    background: linear-gradient(to bottom, var(--grass-light), var(--grass));
  }
  .church-name {
    position: absolute;
    top: 170px;
    left: 0; right: 0;
    text-align: center;
    font-family: "Montserrat", sans-serif;
    font-weight: 800;
    font-size: 58px;
    line-height: 1.18;
    letter-spacing: 1px;
    color: var(--title-ink);
    text-transform: uppercase;
  }
  .info-band {
    position: absolute;
    left: 0; right: 0; bottom: 0;
    height: 178px;
    background: var(--band);
  }
  .service-times {
    position: absolute;
    top: 40px;
    left: 0; right: 0;
    list-style: none;
    text-align: center;
    font-family: "Montserrat", sans-serif;
    font-weight: 600;
    font-size: 22px;
    line-height: 1.55;
    color: var(--info-text);
    text-transform: uppercase;
  }
  .ministry-name {
    position: absolute;
    right: 26px;
    bottom: 26px;
    font-family: "Montserrat", sans-serif;
    font-weight: 600;
    font-size: 16px;
    color: var(--info-text);
  }
</style>
</head>
<body>
  <main class="church-sign">
    <div class="backdrop-art" role="img" aria-label="Illustration of two oak trees arching over three white crosses against a sunlit sky"></div>
    <div class="grass-edge" role="img" aria-label="Illustrated green grass line"></div>
    <h1 class="church-name">Keller Ridge<br>Community Church</h1>
    <section class="info-band">
      <ul class="service-times">
        <li>10:00 AM Worship Service</li>
        <li>9:30 AM Sunday School</li>
        <li>6:00 PM Wednesday Service</li>
      </ul>
      <div class="ministry-name">Ridgeline Ministries</div>
    </section>
  </main>
</body>
</html>
```